"The Wandering Mentor", a Higher Ed blogger, would like a wordpress design

I would like a wordpress design for blogs written by "The Wandering Mentor." that can be easily expanded by me once the initial design is complete.

Here is context which I would like included on the Home/Welcome page: "I started The Wandering Mentor in 2021 to write about the practice of academic advising through the lens of horsemanship. After one year of developing skills as a brand new equestrian, I couldn’t help but notice the similarities between my vocation as an academic advisor and my avocation as a budding equestrian. I hope my musings about my journey in two very different fields will cultivate curiosity, widen your aperture and ignite academic advisors to take their practice to the next level. "

The wordpress will primarily have blogs by myself or guest bloggers writing about academic advising for advisors, but I may widen my audience to include students and families. I'd like to have readers submit questions that I can answer. Depending on interest, I may want to have a section on Horsemanship but that is not truly the focus of this site.

I'd like the feel of the site to be positive, fresh, modern (but not too wild), with the emphasis on Higher Ed/Academic Advising as opposed to equestrian pursuits. I don't want it to feel clunky and blocky like some sites that have to do with education. I'm hoping that readers will have some "aha" moments after reading some of the posts.

I have included my logo files

```html
<!DOCTYPE html>
<html lang="en">
<head>
<meta charset="utf-8">
<title>The Wandering Mentor – Home</title>
<link href="https://fonts.googleapis.com/css2?family=Roboto:wght@300;400;500;700&display=swap" rel="stylesheet">
<style>
:root{
  --gold:#d6ad66;
  --gold-dark:#c99a4e;
  --ink:#222222;
  --text:#444444;
  --muted:#777777;
  --dark:#221f20;
  --line:#dddddd;
  --blue:#2b85c7;
  --teal:#1aa3a8;
  --panel:#f2f2f2;
  --white:#ffffff;
}
*{box-sizing:border-box;margin:0;padding:0}
html,body{width:1200px;height:4959px;overflow:hidden}
body{position:relative;background:var(--white);font-family:"Roboto",Arial,sans-serif;color:var(--text)}
.abs{position:absolute}
a{color:inherit;text-decoration:none}

/* header */
.site-header{position:absolute;left:0;top:0;width:1200px;height:120px;background:var(--white)}
.brand{position:absolute;left:100px;top:30px;display:flex;align-items:center;gap:12px}
.brand-mark{width:40px;height:40px;border-radius:50%;border:2px solid var(--gold)}
.brand-name{font-size:21px;font-weight:400;color:var(--ink)}
.follow{position:absolute;left:593px;top:30px;display:flex;align-items:center;gap:18px;font-size:14px;color:var(--ink)}
.follow .rule{width:42px;height:1px;background:var(--ink)}
.dot-icon{width:12px;height:12px;border-radius:50%;background:var(--ink)}
.join{position:absolute;left:978px;top:19px;width:122px;height:39px;background:var(--gold);color:#fff;font-size:14px;font-weight:500;display:flex;align-items:center;justify-content:center;letter-spacing:.3px}
.nav{position:absolute;top:78px;left:0;font-size:15px;font-weight:500;color:var(--ink)}
.nav a{position:absolute;white-space:nowrap}
.nav .active{color:var(--gold)}

/* hero */
.hero{position:absolute;left:0;top:120px;width:1200px;height:606px;background:linear-gradient(100deg,#5c4a3a 0%,#7a6650 35%,#a08060 55%,#8a5a32 75%,#5e4630 100%)}
.hero-title{position:absolute;left:100px;top:175px;font-size:61px;line-height:60px;font-weight:700;color:#fff;letter-spacing:.5px}
.hero-lead{position:absolute;left:100px;top:313px;width:460px;font-size:14px;line-height:20px;font-weight:500;color:#fff}
.hero-btn{position:absolute;left:100px;top:377px;width:158px;height:44px;background:var(--gold);color:#fff;font-size:14px;font-weight:500;display:flex;align-items:center;justify-content:center}
.hero-dots{position:absolute;left:560px;top:562px;display:flex;gap:12px}
.hero-dots span{width:10px;height:10px;border-radius:50%;border:1.5px solid #fff}
.hero-dots .on{background:#fff}

/* split bands */
.split{position:absolute;left:0;width:1200px;background:var(--dark)}
.split-photo{position:absolute;left:0;top:0;width:600px;height:100%}
.split-body{position:absolute;left:653px;color:#fff}
.split-title{font-size:30px;font-weight:500;color:#fff}
.split-text{font-size:13px;line-height:27.6px;color:#eee;text-align:justify;width:447px}
.read-more{position:absolute;right:0;bottom:0;width:162px;height:45px;background:var(--gold);color:#fff;font-size:14px;font-weight:500;display:flex;align-items:center;justify-content:center}

/* posts */
.post{position:absolute;left:120px;width:646px}
.post-title{position:absolute;left:0;top:0;font-size:26px;font-weight:500;color:var(--ink);white-space:nowrap}
.post-meta{position:absolute;left:0;top:44px;width:646px;font-size:11px;color:var(--ink);display:flex;justify-content:space-between}
.post-photo{position:absolute;left:0;top:64px;width:646px;height:420px;border-radius:4px}
.post-tag{position:absolute;right:10px;top:74px;background:var(--gold);color:#fff;font-size:12px;padding:7px 12px}
.post-card{position:absolute;left:15px;top:439px;width:616px;height:210px;background:#fff}
.post-excerpt{position:absolute;left:17px;top:14px;width:585px;font-size:14px;line-height:25px;color:var(--ink)}
.post-more{position:absolute;left:17px;top:108px;font-size:15px;font-weight:500;color:var(--gold);display:flex;align-items:center;gap:8px}
.share{position:absolute;right:24px;top:100px;display:flex;align-items:center;gap:8px;font-size:12px;color:#aaa;font-weight:500}
.share span.c{width:30px;height:30px;border-radius:50%;background:#cfcfcf}
.ask{position:absolute;left:17px;top:141px;width:138px;height:32px;background:var(--ink);color:#fff;font-size:11px;font-weight:700;display:flex;align-items:center;justify-content:center;border-radius:2px}
.post-rule{position:absolute;left:0;top:655px;width:634px;height:1px;background:#ccc}
.learn{position:absolute;left:274px;top:3338px;font-size:17px;font-weight:500;color:var(--ink);border-bottom:2px solid var(--gold);padding-bottom:4px}

/* sidebar */
.sidebar{position:absolute;left:830px;top:1283px;width:248px}
.post-blog{position:absolute;left:0;top:0;width:248px;height:40px;border:1.5px solid var(--blue);color:var(--blue);font-size:15px;display:flex;align-items:center;justify-content:center}
.updates{position:absolute;left:0;top:52px;width:248px;height:100px;background:var(--panel)}
.updates h4{position:absolute;left:0;top:14px;width:100%;text-align:center;font-size:15px;font-weight:400;color:var(--ink)}
.updates .field{position:absolute;left:10px;top:44px;width:150px;height:34px;background:#fff;font-size:10px;color:#555;padding:11px 10px}
.updates .sub{position:absolute;left:160px;top:44px;width:80px;height:34px;background:var(--gold);color:#fff;font-size:11px;font-weight:500;display:flex;align-items:center;justify-content:center}
.side-social{position:absolute;left:4px;top:175px;width:240px;display:flex;justify-content:space-between;align-items:center}
.side-social .sq{width:14px;height:14px;border-radius:50%;background:#9aa0a6}
.search{position:absolute;left:0;top:210px;width:248px;height:32px;border:1px solid #ccc;font-size:10px;color:#666;padding:10px}
.search svg{position:absolute;right:8px;top:7px}
.side-label{position:absolute;left:2px;top:268px;font-size:14px;color:var(--ink)}
.side-card{position:absolute;left:0;top:293px;width:248px;height:322px;border:1px solid #e6e6e6;background:#fff}
.side-card .photo{position:absolute;left:0;top:0;width:248px;height:148px;background:linear-gradient(180deg,#9cc1dc 0%,#b9cfa0 45%,#6e8f45 70%,#8a6a3c 100%)}
.side-card h5{position:absolute;left:10px;top:160px;width:230px;font-size:14px;font-weight:400;line-height:20px;color:var(--ink)}
.side-card p{position:absolute;left:14px;top:207px;width:225px;font-size:10px;line-height:20px;color:#777}
.side-card .btn{position:absolute;left:12px;top:276px;width:100px;height:30px;background:#ddd;font-size:11px;color:#555;display:flex;align-items:center;justify-content:center}
.side-head{position:absolute;left:0;font-size:13px;font-weight:500;color:var(--blue)}
.side-item{position:absolute;left:0;font-size:11px;color:var(--ink)}
.side-link{position:absolute;left:0;font-size:13px;color:var(--teal)}
.pop{position:absolute;left:0;width:248px;font-size:12px;line-height:21px;color:var(--ink)}
.pop.teal{color:var(--teal)}
.pop small{display:block;font-size:12px;color:#777}
.pop .stats{font-size:11px;color:var(--ink)}
.cta{position:absolute;left:0;top:1109px;width:248px;height:216px;background:var(--panel)}
.cta p{position:absolute;left:14px;top:28px;width:224px;font-size:16px;line-height:28px;color:var(--ink)}
.cta .btn{position:absolute;left:14px;top:149px;width:188px;height:37px;background:var(--gold);color:#fff;font-size:14px;font-weight:500;display:flex;align-items:center;justify-content:center}

/* why */
.why-title{position:absolute;left:0;top:3986px;width:1200px;text-align:center;font-size:36px;font-weight:500;color:var(--ink)}
.why-sub{position:absolute;left:0;top:4044px;width:1200px;text-align:center;font-size:16px;color:var(--ink)}
.feature{position:absolute;top:4126px;width:340px;text-align:center}
.feature svg{display:block;margin:0 auto}
.feature h3{margin-top:38px;font-size:18px;font-weight:500;color:var(--ink);letter-spacing:.3px}
.feature p{margin-top:16px;font-size:15px;line-height:25px;color:var(--ink)}

/* footer */
.site-footer{position:absolute;left:0;top:4461px;width:1200px;height:498px;background:var(--dark);color:#fff}
.news-title{position:absolute;left:100px;top:92px;font-size:23px;font-weight:500}
.news-text{position:absolute;left:100px;top:150px;width:480px;font-size:13px;line-height:19px;color:#eee}
.input{position:absolute;left:100px;width:476px;height:41px;background:#fff;color:#444;font-size:13px;padding:12px 14px}
.check{position:absolute;left:100px;top:4792px;font-size:11px;color:#eee;display:flex;align-items:center;gap:6px}
.check i{width:11px;height:11px;background:#fff;display:inline-block}
.submit{position:absolute;left:458px;top:327px;width:118px;height:42px;background:var(--gold);color:#fff;font-size:15px;font-weight:500;display:flex;align-items:center;justify-content:center}
.foot-brand{position:absolute;left:636px;top:98px;display:flex;flex-direction:column;align-items:center;width:96px;gap:6px}
.foot-brand .ring{width:52px;height:52px;border-radius:50%;border:2px solid #fff}
.foot-brand span{font-size:10px;text-align:center;line-height:13px}
.about-head{position:absolute;left:749px;top:101px;font-size:14px;font-weight:500;color:var(--gold)}
.about-text{position:absolute;left:749px;top:124px;width:360px;font-size:13px;line-height:24.5px;color:#eee}
.foot-social{position:absolute;left:744px;top:331px;display:flex;gap:28px;align-items:center}
.foot-social .c{width:16px;height:16px;border-radius:50%;background:#fff}
.copyright{position:absolute;left:0;top:460px;width:1200px;text-align:center;font-size:13px;color:#eee}
</style>
</head>
<body>

<header class="site-header">
  <a class="brand" href="#"><span class="brand-mark"></span><span class="brand-name">The Wandering Mentor</span></a>
  <div class="follow">
    <span>Follow on</span><span class="rule"></span>
    <span class="dot-icon"></span><span class="dot-icon"></span><span class="dot-icon"></span><span class="dot-icon"></span><span class="dot-icon"></span>
    <svg width="14" height="11" viewBox="0 0 14 11"><rect x=".5" y=".5" width="13" height="10" fill="#222"/><path d="M1 1l6 5 6-5" stroke="#fff" fill="none"/></svg>
    <svg width="13" height="13" viewBox="0 0 13 13"><circle cx="5.5" cy="5.5" r="4.3" stroke="#222" stroke-width="1.8" fill="none"/><path d="M8.6 8.6L12 12" stroke="#222" stroke-width="1.8"/></svg>
  </div>
  <a class="join" href="#">JOIN NOW</a>
  <nav class="nav">
    <a class="active" style="left:472px">HOME</a>
    <a style="left:603px">ABOUT</a>
    <a style="left:741px">SERVICES</a>
    <a style="left:900px">BLOG</a>
    <a style="left:1025px">CONTACT</a>
  </nav>
</header>

<section class="hero" role="img" aria-label="Rider galloping a chestnut horse across a sunlit arena">
  <h1 class="hero-title">THE WANDERING<br>MENTOR</h1>
  <p class="hero-lead">Lorem ipsum dolor sit amet, consectetur adipiscing elit, sed do eiusmod tempor incididunt ut labore et dolore</p>
  <a class="hero-btn" href="#">GET STARTED</a>
  <svg class="abs" style="left:56px;top:270px" width="20" height="36" viewBox="0 0 20 36"><path d="M18 2L3 18l15 16" stroke="#fff" stroke-width="2" fill="none"/></svg>
  <svg class="abs" style="left:1114px;top:270px" width="20" height="36" viewBox="0 0 20 36"><path d="M2 2l15 16L2 34" stroke="#fff" stroke-width="2" fill="none"/></svg>
  <div class="hero-dots"><span></span><span class="on"></span><span></span><span></span></div>
</section>

<section class="split" style="top:726px;height:432px">
  <div class="split-photo" role="img" aria-label="Advisor and student reviewing paperwork together at a table" style="background:linear-gradient(120deg,#8a7d6a 0%,#c8b9a0 40%,#6f8fa8 70%,#4a3a30 100%)"></div>
  <div class="split-body" style="top:80px">
    <h2 class="split-title">Welcome The Wandering Mentor</h2>
    <p class="split-text" style="margin-top:18px">I started The Wandering Mentor in 2021 to write about the practice of academic advising through the lens of horsemanship. After one year of developing skills as a brand new equestrian, I couldn’t help but notice the similarities between my vocation as an academic advisor and my avocation as a budding equestrian. I hope my musings about my journey in two very different fields will cultivate curiosity, widen your aperture and ignite academic advisors to take their practice to the next level.</p>
  </div>
  <a class="read-more" href="#">READ MORE</a>
</section>

<!-- blog posts -->
<article class="post" style="top:1248px">
  <h2 class="post-title">Sed ut perspiciatis unde omnis iste natus error sit</h2>
  <div class="post-meta"><span>John Smith &nbsp;|&nbsp; August 8, 2021</span><span>688,329 Views &nbsp;|&nbsp; 5 comments &nbsp;|&nbsp; 3 likes</span></div>
  <div class="post-photo" role="img" aria-label="Smiling rider on a bay horse outdoors" style="background:linear-gradient(180deg,#eef0ea 0%,#d8dccf 40%,#8a6a48 65%,#6f8a3e 100%)"></div>
  <span class="post-tag">Budding Equestrian</span>
  <div class="post-card">
    <p class="post-excerpt">Lorem ipsum dolor sit amet, consectetur adipiscing elit, sed do eiusmod tempor incididunt ut labore et dolore magna aliqua. Quisqsum suspendisse ultrices gravida. Risus commodo viverra maecenas accumsan lacus vel facilisis.....</p>
    <a class="post-more" href="#">Read More <svg width="20" height="10" viewBox="0 0 20 10"><path d="M0 5h18M14 1l4 4-4 4" stroke="#d6ad66" fill="none" stroke-width="1.3"/></svg></a>
    <div class="share">SHARE <span class="c"></span><span class="c"></span><span class="c"></span></div>
    <a class="ask" href="#">Ask Questions?</a>
  </div>
  <div class="post-rule"></div>
</article>

<article class="post" style="top:1934px">
  <h2 class="post-title">Sed ut perspiciatis unde omnis iste natus error sit</h2>
  <div class="post-meta"><span>John Smith &nbsp;|&nbsp; August 8, 2021</span><span>688,329 Views &nbsp;|&nbsp; 5 comments &nbsp;|&nbsp; 3 likes</span></div>
  <div class="post-photo" role="img" aria-label="Two students laughing while studying at a desk" style="background:linear-gradient(100deg,#b8a99a 0%,#e2d8cf 35%,#8fb6d0 55%,#2a4fa8 80%,#3a2e2a 100%)"></div>
  <span class="post-tag">Academic Advisor</span>
  <div class="post-card">
    <p class="post-excerpt">Lorem ipsum dolor sit amet, consectetur adipiscing elit, sed do eiusmod tempor incididunt ut labore et dolore magna aliqua. Quisqsum suspendisse ultrices gravida. Risus commodo viverra maecenas accumsan lacus vel facilisis.....</p>
    <a class="post-more" href="#">Read More <svg width="20" height="10" viewBox="0 0 20 10"><path d="M0 5h18M14 1l4 4-4 4" stroke="#d6ad66" fill="none" stroke-width="1.3"/></svg></a>
    <div class="share">SHARE <span class="c"></span><span class="c"></span><span class="c"></span></div>
    <a class="ask" href="#">Ask Questions?</a>
  </div>
  <div class="post-rule"></div>
</article>

<article class="post" style="top:2620px">
  <h2 class="post-title">Sed ut perspiciatis unde omnis iste natus error sit</h2>
  <div class="post-meta"><span>John Smith &nbsp;|&nbsp; August 8, 2021</span><span>688,329 Views &nbsp;|&nbsp; 5 comments &nbsp;|&nbsp; 3 likes</span></div>
  <div class="post-photo" role="img" aria-label="Rider and horse clearing a show jump beneath mountains" style="background:linear-gradient(180deg,#a9c6e6 0%,#c9dbee 30%,#8a93a0 45%,#7a8a5a 62%,#5a4330 85%,#3b4f8a 100%)"></div>
  <span class="post-tag">Budding Equestrian</span>
  <div class="post-card">
    <p class="post-excerpt">Lorem ipsum dolor sit amet, consectetur adipiscing elit, sed do eiusmod tempor incididunt ut labore et dolore magna aliqua. Quisqsum suspendisse ultrices gravida. Risus commodo viverra maecenas accumsan lacus vel facilisis.....</p>
    <a class="post-more" href="#">Read More <svg width="20" height="10" viewBox="0 0 20 10"><path d="M0 5h18M14 1l4 4-4 4" stroke="#d6ad66" fill="none" stroke-width="1.3"/></svg></a>
    <div class="share">SHARE <span class="c"></span><span class="c"></span><span class="c"></span></div>
    <a class="ask" href="#">Ask Questions?</a>
  </div>
  <div class="post-rule"></div>
</article>

<a class="learn" href="#">Learn More About The Wandering Mentor</a>

<!-- sidebar -->
<aside class="sidebar">
  <a class="post-blog" href="#">Post a Blog</a>
  <div class="updates">
    <h4>Send Me Updates</h4>
    <div class="field">Enter email address</div>
    <div class="sub">Subscribe</div>
  </div>
  <div class="side-social"><span class="sq"></span><span class="sq"></span><span class="sq"></span><span class="sq"></span><span class="sq"></span>
    <svg width="16" height="12" viewBox="0 0 16 12"><rect x=".5" y=".5" width="15" height="11" fill="#9aa0a6"/><path d="M1 1l7 5 7-5" stroke="#fff" fill="none"/></svg>
  </div>
  <div class="search">Looking for something.....
    <svg width="16" height="16" viewBox="0 0 16 16"><circle cx="7" cy="7" r="5" stroke="#555" stroke-width="1.4" fill="none"/><path d="M10.6 10.6L15 15" stroke="#555" stroke-width="1.4"/></svg>
  </div>
  <div class="side-label">vocation as a budding equestrian</div>
  <div class="side-card">
    <div class="photo" role="img" aria-label="Instructor guiding a rider on a horse in a green field"></div>
    <h5>Lorem ipsr sit amet, consectetur adipiscing elit, sed do</h5>
    <p>Lorem ipsum dolor sit ameectetur adipiscing elit, sed do eiusmodor incididunt ut labore et dolore magna aliqua.</p>
    <a class="btn" href="#">Read More</a>
  </div>
  <div class="side-head" style="top:642px">TOP CATEGORY</div>
  <div class="side-item" style="top:667px">erspiciatis unde omnis</div>
  <div class="side-item" style="top:692px">Finibus Bonorum et</div>
  <div class="side-link" style="top:726px">Tips for budding equestrian</div>
  <div class="side-item" style="top:752px">erspiciatis unde omnis</div>
  <div class="side-item" style="top:777px">Finibus Bonorum et</div>
  <div class="side-head" style="top:814px">POPULAR POST</div>
  <div class="pop" style="top:838px">Lorem ipsum dolor sit amet,cur adipiscing elit, sed do eiusmod teor incididunt ut labore et dolore magna aliqua.<small>John Smith</small><span class="stats">688,329 Views &nbsp;|&nbsp; 5 comments &nbsp;|&nbsp; 3 likes</span></div>
  <div class="pop teal" style="top:966px">Lorem ipsum dolor sit amet,cur adipiscing elit, sed do eiusmod teor incididunt ut labore et dolore magna aliqua.<small>John Smith</small><span class="stats">688,329 Views &nbsp;|&nbsp; 5 comments &nbsp;|&nbsp; 3 likes</span></div>
  <div class="cta">
    <p>Sed ut perspciatis unde omnis ste natus error sit voluptatem accusantium doloremque laudantium, totam rem aperm</p>
    <a class="btn" href="#">Get Started</a>
  </div>
</aside>

<section class="split" style="top:3465px;height:431px">
  <div class="split-photo" role="img" aria-label="Rider leading a horse in a fenced autumn paddock" style="background:linear-gradient(110deg,#d9d2c4 0%,#b59a7a 35%,#7a4a2a 60%,#c9c0b0 100%)"></div>
  <div class="split-body" style="top:80px">
    <h2 class="split-title" style="font-size:33px">Horsemanship</h2>
    <p class="split-text" style="margin-top:18px;line-height:27.5px">Lorem ipsum dolor sit amet, consectetur adipiscing elit, sed do eiusmod tempor incididunt ut labore et dolore magna ipsum suspendisse ultrices gravida. Risus commodo viverra maecenas accumsan lacus vel facilisis. Lorem ipsum dolor sit amet, consectetur adipiscing elit, sed do eiusmod tempor incididunt ut labore et doloqua. Quis ipsum suspendisse ultrices gravida. Risus commodo viverra maecenas</p>
    <p style="margin-top:32px;margin-left:8px;font-size:14px;color:#fff">14 SPE 2021, 10: 00 AM</p>
  </div>
  <a class="read-more" href="#">READ MORE</a>
</section>

<h2 class="why-title">Why The Wandering Mentor</h2>
<p class="why-sub">sit voluptatem accusantium doloremque laudantium totam rem aperiam</p>

<div class="feature" style="left:80px">
  <svg width="76" height="72" viewBox="0 0 76 72" fill="none" stroke="#d6ad66" stroke-width="2">
    <circle cx="38" cy="14" r="7"/><circle cx="18" cy="22" r="6"/><circle cx="58" cy="22" r="6"/>
    <path d="M26 38c0-8 5-13 12-13s12 5 12 13"/><path d="M8 44c0-7 4-11 10-11 3 0 5 1 7 3M68 44c0-7-4-11-10-11-3 0-5 1-7 3"/>
    <path d="M6 56l14-8 10 6h14l10-6 14 8M22 50l12 10h8l12-10"/>
  </svg>
  <h3>FINIBUS BONORUM ET</h3>
  <p>Lorem ipsum dolor sit amet, ecttur adipiscing elit, sed do eiusd tempor incididunt ut labore et doloreagna alua. Quis ipsum suspendisse ultrs gravida. Risus codo viverra</p>
</div>
<div class="feature" style="left:429px">
  <svg width="82" height="70" viewBox="0 0 82 70" fill="none" stroke="#d6ad66" stroke-width="2">
    <path d="M41 6L4 22l37 16 37-16z"/><path d="M20 30v18c0 8 42 8 42 0V30"/><path d="M70 25v24"/><rect x="66" y="49" width="8" height="10"/>
  </svg>
  <h3>FINIBUS BONORUM ET</h3>
  <p>Lorem ipsum dolor sit amet, ecttur adipiscing elit, sed do eiusd tempor incididunt ut labore et doloreagna alua. Quis ipsum suspendisse ultrs gravida. Risus codo viverra</p>
</div>
<div class="feature" style="left:776px">
  <svg width="80" height="72" viewBox="0 0 80 72" fill="none" stroke="#d6ad66" stroke-width="2">
    <path d="M40 4l16 6v12c0 10-7 17-16 21-9-4-16-11-16-21V10z"/><path d="M32 22l6 6 11-11"/>
    <path d="M4 52l12-6h16l10 4h14l14-6c3 0 4 3 2 5L52 64H26l-10-4H4"/>
  </svg>
  <h3>FINIBUS BONORUM ET</h3>
  <p>Lorem ipsum dolor sit amet, ecttur adipiscing elit, sed do eiusd tempor incididunt ut labore et doloreagna alua. Quis ipsum suspendisse ultrs gravida. Risus codo viverra</p>
</div>

<footer class="site-footer">
  <h2 class="news-title">Sign Up to The Wandering Mentor Newsletter!</h2>
  <p class="news-text">Enter your email and ge the very latest news from The Wandering Mentor: tips and insights, announcements, events, and more! Sign up now!</p>
  <div class="input" style="top:210px">Email</div>
  <div class="input" style="top:267px">Phone</div>
  <a class="submit" href="#">SUBMIT</a>
  <div class="foot-brand"><span class="ring"></span><span>The Wandering Mentor</span></div>
  <h3 class="about-head">ABOUT THE WANDERING MENTOR</h3>
  <p class="about-text">Lorem ipsum dolor sit amet, consectetur adipiscing elit, sed do eiusmod tempor incididunt ut labore et doagna aliqua. Ut enim ad minim veniam, quis nostrud exercitan ullamco laboris nisi ut aliquip ex ea commodo consequat . Duis aute irure dolor in reprehenderit in voluptate velsse cillum dolore eu fugiat nulla pariatur. Excepteur sint aecat cupidatat non proident, sunt in culpa</p>
  <div class="foot-social">
    <svg width="22" height="22" viewBox="0 0 22 22" fill="#fff"><circle cx="17" cy="4" r="3.5"/><circle cx="5" cy="11" r="3.5"/><circle cx="17" cy="18" r="3.5"/><path d="M5 11L17 4M5 11l12 7" stroke="#fff" stroke-width="2"/></svg>
    <span class="c"></span><span class="c"></span><span class="c"></span><span class="c"></span><span class="c"></span>
    <svg width="18" height="13" viewBox="0 0 18 13"><rect width="18" height="13" fill="#fff"/><path d="M1 1l8 6 8-6" stroke="#221f20" fill="none" stroke-width="1.3"/></svg>
  </div>
  <p class="copyright">Copyright © 2021 The Wandering Mentor All rights reserved.</p>
</footer>
<div class="check"><i></i>Send me news and updates</div>

</body>
</html>
```